| バナーサイズ |
| 現在のヘッダーデザインにとらわれず、サイトイメージとマッチするような、 オリジナルのヘッダーを作成して下さい。 ■サイズ ヘッダー画像サイズ:横幅1450px、縦幅680px 対象サイト:http://www.vormeta-k.com ■会社(サービス)概要 企業向けのコンサルティングサービス、各種ビジネスサービスを展開しています。 主に中小企業、中堅企業向けのクライアントが対象 ■利用客層 男性メイン 特に、課長/部長等のマネージメントクラス、役員/経営者向け ■最後に ご質問あれば、回答させて頂きます。 一人で複数の応募も問題ございません。 多くの方からの、ご応募をお待ちしています。 |

```html
<!DOCTYPE html>
<html lang="ja">
<head>
<meta charset="utf-8">
<title>Vormeta Group ヘッダー</title>
<link rel="stylesheet" href="https://fonts.googleapis.com/css2?family=Noto+Sans+JP:wght@500;700;900&display=swap">
<style>
  :root {
    --nav-bg: #d9625a;
    --nav-text: #ffffff;
    --brand: #1c2a6b;
    --hero-deep: #14207a;
    --hero-mid: #2b3fa8;
    --hero-dark: #111318;
    --band: #0a0b0e;
    --text-white: #ffffff;
    --accent-yellow: #ffe14a;
  }
  * { margin: 0; padding: 0; box-sizing: border-box; }
  html, body {
    width: 1200px; height: 662px; overflow: hidden;
    font-family: "Noto Sans JP", sans-serif;
    background: #000;
  }
  .header {
    position: relative; width: 1200px; height: 662px; overflow: hidden;
  }
  .site-nav {
    position: absolute; top: 0; left: 0; width: 1200px; height: 96px;
    background: var(--nav-bg);
    display: flex; align-items: center;
    z-index: 2;
  }
  .brand {
    position: absolute; left: 100px; top: 22px;
    display: flex; align-items: center; gap: 8px;
    color: var(--brand); font-weight: 700; font-size: 15px;
  }
  .brand-mark {
    width: 34px; height: 34px; border-radius: 50%; background: var(--brand);
  }
  .nav-list {
    position: absolute; left: 280px; top: 36px;
    list-style: none; display: flex;
  }
  .nav-list li {
    color: var(--nav-text); font-size: 13px; font-weight: 500;
    margin-right: 58px; white-space: nowrap;
  }
  .hero-photo {
    position: absolute; top: 96px; left: 0; width: 1200px; height: 566px;
    background:
      radial-gradient(ellipse 140px 120px at 610px 255px, rgba(255,255,255,0.35), rgba(255,255,255,0) 70%),
      linear-gradient(90deg, var(--hero-deep) 0%, var(--hero-mid) 35%, #3a4170 55%, #2a2c36 72%, var(--hero-dark) 100%);
  }
  .hero-shade {
    position: absolute; left: 0; top: 500px; width: 1200px; height: 162px;
    background: linear-gradient(180deg, rgba(10,11,14,0) 0%, rgba(10,11,14,0.85) 45%, var(--band) 100%);
  }
  .headline {
    position: absolute; left: 24px; top: 305px;
    color: var(--text-white); font-weight: 900; font-size: 36px; line-height: 68px;
    letter-spacing: 0.5px;
    text-shadow: 2px 2px 0 #000, 0 0 6px rgba(0,0,0,0.8);
    white-space: nowrap;
  }
  .intro {
    position: absolute; left: 24px; top: 596px;
    color: var(--text-white); font-weight: 700; font-size: 13.5px; line-height: 32px;
    white-space: nowrap;
  }
  .intro .service { color: var(--accent-yellow); }
</style>
</head>
<body>
<header class="header">
  <nav class="site-nav">
    <div class="brand"><span class="brand-mark"></span><span class="brand-name">Vormeta Group</span></div>
    <ul class="nav-list">
      <li>サービス一覧</li>
      <li>お客様の成功事例</li>
      <li>実績一覧</li>
      <li>Blog</li>
      <li>会社概要</li>
      <li>お問い合わせ</li>
    </ul>
  </nav>
  <div class="hero-photo" role="img" aria-label="スーツ姿のビジネスマンが光るタッチパネルを指先で操作している写真、青い背景"></div>
  <div class="hero-shade"></div>
  <h1 class="headline">私たちは事業の課題を明確にし、<br>解決するプロセスで組織の成長とイノベーションを成し遂げます</h1>
  <p class="intro">IT通信、ソフトウェア、人材、流通、小売、金融サービス、製造、専門サービスなど、多くの業界で事業改善を実現してきました。<br><span class="service">「新規事業策定」「業務改善」「営業/マーケティング戦略策定」「CRM」「ERP」</span>など戦略業務や業務効率化するシステムの導入、運用でお客様をサポートさせていただきます。</p>
</header>
</body>
</html>
```